VORN - Business cards

Business card to be created for Commercial sales staff

Target Market(s)

Commercial businesses

Industry/Entity Type

Commercial

Contact Information for Business Card

Look professional. For commercial clients

Colors
ffffff

Requirements
Must have
• - Vorn Logo
• - Commercial sales staff as postion
• - room for commerical sales manager role
• - person name and their mobile number
• - Website : vornelectrical.com.au
Nice to have
• White background.
• On back of business card just have the logo no other information
Should not have
• Should only have white background on front of card.

```html
<!DOCTYPE html>
<html lang="en">
<head>
<meta charset="utf-8">
<title>VORN – Business Card</title>
<link rel="stylesheet" href="https://fonts.googleapis.com/css2?family=Merriweather:wght@400;700;900&display=swap">
<style>
  :root {
    --canvas: #d9d9d9;
    --card-white: #ffffff;
    --brand-red: #c62127;
    --ink: #24262b;
    --muted: #8a8a8a;
    --band-black: #111111;
  }
  * { margin: 0; padding: 0; box-sizing: border-box; }
  html, body {
    width: 1200px; height: 1200px; overflow: hidden;
    background: var(--canvas);
    font-family: "Merriweather", Georgia, serif;
  }
  .sheet {
    position: relative; width: 1200px; height: 1200px;
    display: flex; flex-direction: column; align-items: center; justify-content: center; gap: 60px;
  }
  .card {
    position: relative; width: 840px; height: 498px; overflow: hidden;
    box-shadow: 0 6px 18px rgba(0,0,0,.18);
  }
  .card--front { background: var(--card-white); color: var(--ink); }
  .card--back { background: var(--brand-red); }

  .brand {
    position: absolute; display: flex; align-items: center; gap: 18px;
    font-family: "Merriweather", Georgia, serif; font-weight: 900; letter-spacing: 2px; line-height: 1;
  }
  .brand__dot { border-radius: 50%; flex: none; }
  .card--front .brand { top: 62px; right: 44px; font-size: 84px; color: var(--ink); }
  .card--front .brand__dot { width: 40px; height: 40px; background: var(--brand-red); }
  .card--back .brand { top: 50%; left: 50%; transform: translate(-50%, -50%); font-size: 110px; color: var(--ink); }
  .card--back .brand__dot { width: 52px; height: 52px; background: var(--card-white); }

  .person { position: absolute; left: 48px; top: 186px; }
  .person__name { font-size: 28px; font-weight: 700; }
  .person__role { font-size: 19px; color: var(--muted); margin-top: 4px; }

  .contacts { position: absolute; left: 48px; top: 306px; list-style: none; font-size: 22px; line-height: 33px; }
  .contacts li { display: flex; align-items: flex-start; gap: 12px; }
  .contacts svg { width: 24px; height: 24px; flex: none; margin-top: 4px; }
  .contacts .indent { padding-left: 36px; }

  .website { position: absolute; right: 44px; bottom: 36px; font-size: 22px; font-weight: 700; }

  .band { position: absolute; left: 0; right: 0; bottom: 0; height: 20px; display: flex; }
  .band__dark { flex: 1; background: var(--band-black); }
  .band__red { flex: 1; background: var(--brand-red); }
</style>
</head>
<body>
<main class="sheet">
  <section class="card card--front" aria-label="Business card front">
    <div class="brand"><span class="brand__dot"></span><span class="brand__name">VORN</span></div>

    <div class="person">
      <p class="person__name">Name Here</p>
      <p class="person__role">Position Here</p>
    </div>

    <ul class="contacts">
      <li>
        <svg viewBox="0 0 24 24" aria-hidden="true"><circle cx="12" cy="12" r="12" fill="#24262b"/><rect x="8.5" y="5" width="7" height="14" rx="1.5" fill="#fff"/><rect x="9.8" y="7" width="4.4" height="8" fill="#24262b"/></svg>
        <span>000 0000 0000</span>
      </li>
      <li>
        <svg viewBox="0 0 24 24" aria-hidden="true"><circle cx="12" cy="12" r="12" fill="#24262b"/><path d="M6 10c0-2 3-3 6-3s6 1 6 3v1h-3V9.5h-6V11H6z" fill="#fff"/><rect x="8" y="12" width="8" height="6" rx="1" fill="#fff"/></svg>
        <span>000 0000 0000</span>
      </li>
      <li>
        <svg viewBox="0 0 24 24" aria-hidden="true"><circle cx="12" cy="12" r="12" fill="#24262b"/><rect x="6" y="8" width="12" height="8" rx="1" fill="#fff"/><path d="M6.5 8.5 12 13l5.5-4.5" fill="none" stroke="#24262b" stroke-width="1.2"/></svg>
        <span>name@vornelectrical.com.au</span>
      </li>
      <li>
        <svg viewBox="0 0 24 24" aria-hidden="true"><circle cx="12" cy="12" r="12" fill="#24262b"/><path d="M12 5a4.5 4.5 0 0 0-4.5 4.5C7.5 13 12 19 12 19s4.5-6 4.5-9.5A4.5 4.5 0 0 0 12 5z" fill="#fff"/><circle cx="12" cy="9.5" r="1.6" fill="#24262b"/></svg>
        <span>Unit, Street</span>
      </li>
      <li class="indent"><span>City, State Postcode</span></li>
    </ul>

    <p class="website">www.vornelectrical.com.au</p>

    <div class="band"><span class="band__dark"></span><span class="band__red"></span></div>
  </section>

  <section class="card card--back" aria-label="Business card back">
    <div class="brand"><span class="brand__dot"></span><span class="brand__name">VORN</span></div>
  </section>
</main>
</body>
</html>
```